Brenway Productions photography and video creator

I need a business card for my production company. I shoot photography and videography for real estate, adventure sports and businesses

simple not to busy

Colors

Designer to choose colors to be used in the design.

Requirements
Must have
• dara@brenwayproductions.ca
• phone -5803317264
• instagram dara_brenway

```html
<!DOCTYPE html>
<html lang="en">
<head>
<meta charset="utf-8">
<title>Brenway Productions – Business Card</title>
<link rel="stylesheet" href="https://fonts.googleapis.com/css2?family=Montserrat:wght@400;500;600;700&display=swap">
<style>
  :root {
    --page: #e9e9e7;
    --card: #ffffff;
    --ink: #1c1c1c;
    --ink-soft: #6e6e6e;
    --forest: #1f1f1f;
    --forest-fade: rgba(31, 31, 31, 0);
    --divider: #2a2a2a;
  }
  * { margin: 0; padding: 0; box-sizing: border-box; }
  html, body {
    width: 1200px;
    height: 900px;
    overflow: hidden;
    background: var(--page);
    font-family: "Montserrat", sans-serif;
    color: var(--ink);
  }
  .canvas { position: relative; width: 1200px; height: 900px; }

  .card {
    position: absolute;
    width: 600px;
    height: 343px;
    background: var(--card);
    box-shadow: 0 6px 18px rgba(0, 0, 0, 0.18);
    overflow: hidden;
  }
  .card--front { left: 120px; top: 80px; }
  .card--back  { left: 480px; top: 475px; }

  .brand {
    position: absolute;
    display: flex;
    align-items: center;
    gap: 12px;
    left: 50%;
    transform: translateX(-50%);
    white-space: nowrap;
  }
  .brand__dot {
    width: 26px; height: 26px;
    border-radius: 50%;
    background: var(--ink);
  }
  .brand__name {
    font-weight: 700;
    letter-spacing: 0.12em;
    color: var(--ink);
    text-transform: uppercase;
  }
  .card--front .brand { top: 128px; }
  .card--front .brand__name { font-size: 24px; }
  .card--back .brand { top: 48px; }
  .card--back .brand__name { font-size: 18px; }
  .card--back .brand__dot { width: 20px; height: 20px; }

  .treeline {
    position: absolute;
    left: 0; right: 0; bottom: 0;
    height: 46px;
    background: linear-gradient(to top, var(--forest) 0%, var(--forest) 35%, var(--forest-fade) 100%);
  }

  .person {
    position: absolute;
    right: 318px;
    top: 186px;
    text-align: right;
  }
  .person__name { font-size: 30px; font-weight: 600; line-height: 1.05; }
  .person__first { color: var(--ink-soft); }
  .person__last { color: var(--ink); }
  .person__role { font-size: 19px; font-weight: 500; margin-top: 4px; }

  .divider {
    position: absolute;
    left: 300px;
    top: 150px;
    width: 1.5px;
    height: 84px;
    background: var(--divider);
  }

  .contact {
    position: absolute;
    left: 318px;
    top: 150px;
    list-style: none;
    font-size: 16px;
    font-weight: 400;
    line-height: 27px;
  }
  .contact__item { display: flex; align-items: center; gap: 8px; }
  .contact__icon { width: 14px; height: 14px; flex: none; }
  .contact__square {
    width: 13px; height: 13px;
    border: 1.6px solid var(--ink);
    border-radius: 3px;
    flex: none;
  }
</style>
</head>
<body>
<main class="canvas">

  <section class="card card--front" aria-label="Business card front">
    <div class="brand">
      <span class="brand__dot"></span>
      <span class="brand__name">Brenway Productions</span>
    </div>
    <div class="treeline" role="img" aria-label="Row of dark pine tree silhouettes along the bottom edge"></div>
  </section>

  <section class="card card--back" aria-label="Business card back">
    <div class="brand">
      <span class="brand__dot"></span>
      <span class="brand__name">Brenway Productions</span>
    </div>

    <div class="person">
      <p class="person__name"><span class="person__first">Dara</span> <span class="person__last">Brenway</span></p>
      <p class="person__role">Manager</p>
    </div>

    <div class="divider"></div>

    <ul class="contact">
      <li class="contact__item">
        <svg class="contact__icon" viewBox="0 0 24 24" aria-hidden="true">
          <path fill="#1c1c1c" d="M6.6 10.8a15.1 15.1 0 0 0 6.6 6.6l2.2-2.2a1 1 0 0 1 1-.25 11.4 11.4 0 0 0 3.6.57 1 1 0 0 1 1 1V20a1 1 0 0 1-1 1A17 17 0 0 1 3 4a1 1 0 0 1 1-1h3.5a1 1 0 0 1 1 1c0 1.25.2 2.46.57 3.6a1 1 0 0 1-.25 1z"/>
        </svg>
        <span>5803317264</span>
      </li>
      <li class="contact__item">
        <span class="contact__square" aria-hidden="true"></span>
        <span>dara_brenway</span>
      </li>
      <li class="contact__item">
        <svg class="contact__icon" viewBox="0 0 24 24" aria-hidden="true">
          <path fill="#1c1c1c" d="M2 5h20v14H2z"/>
          <path fill="none" stroke="#fff" stroke-width="1.8" d="M3 6l9 7 9-7"/>
        </svg>
        <span>dara@brenwayproductions.ca</span>
      </li>
    </ul>

    <div class="treeline" role="img" aria-label="Row of dark pine tree silhouettes along the bottom edge"></div>
  </section>

</main>
</body>
</html>
```